Bloom Ferry Kite Business cards

Logo, tag line and photo on card
Agent Name
Title
Address
Phone number
Email
Website
Make logo on one side large by rotating  to portrait format.  Keep the background of the logo white.

Contact Information for Business Card
Slogan; Keeping Each Kite Aloft

```html
<!DOCTYPE html>
<html lang="en">
<head>
<meta charset="utf-8">
<title>Bloom Ferry Kite – Business Cards</title>
<link rel="stylesheet" href="https://fonts.googleapis.com/css2?family=Open+Sans:wght@400;700&display=swap">
<style>
  :root {
    --navy: #1f2d66;
    --red: #c8202f;
    --ink: #2a2a2a;
    --paper: #ffffff;
    --backdrop: #e9e6e2;
  }
  * { box-sizing: border-box; margin: 0; padding: 0; }
  html, body { width: 1200px; height: 780px; overflow: hidden; }
  body {
    background: var(--backdrop);
    font-family: "Open Sans", Arial, sans-serif;
    color: var(--ink);
    position: relative;
  }
  .card {
    position: absolute;
    left: 285px;
    width: 630px;
    height: 360px;
    background: var(--paper);
    border-radius: 26px;
    box-shadow: 0 6px 18px rgba(0,0,0,0.18);
    overflow: hidden;
  }
  .card--front { top: 20px; }
  .card--back { top: 400px; }

  .profile { position: absolute; left: 44px; top: 26px; width: 300px; }
  .portrait {
    width: 112px; height: 112px;
    margin-left: 100px;
    border-radius: 50%;
    border: 2px solid var(--navy);
    background: radial-gradient(circle at 50% 40%, #9a8a80 0%, #6d645e 45%, #3b3a3d 100%);
  }
  .agent-name {
    margin-top: 10px;
    font-weight: 700;
    font-size: 24px;
    letter-spacing: 0.5px;
    color: var(--red);
    text-transform: uppercase;
    line-height: 1.15;
  }
  .agent-title { font-size: 14px; margin-bottom: 6px; }
  .contact-list { list-style: none; font-size: 14px; line-height: 1.5; }
  .contact-list li { display: flex; align-items: center; gap: 6px; }
  .contact-list svg { width: 12px; height: 12px; flex: none; }
  .address { font-size: 14px; line-height: 1.45; margin-top: 2px; }

  .brand {
    position: absolute;
    display: flex;
    flex-direction: column;
    align-items: center;
  }
  .brand-lockup { display: flex; align-items: center; gap: 10px; }
  .brand-mark { background: var(--red); flex: none; }
  .brand-name {
    font-family: "Open Sans", Arial, sans-serif;
    font-weight: 700;
    color: var(--navy);
    white-space: nowrap;
    line-height: 1.2;
  }
  .brand-tagline {
    font-family: "Open Sans", Arial, sans-serif;
    font-weight: 400;
    color: var(--ink);
  }

  .card--front .brand { right: 40px; bottom: 48px; }
  .card--front .brand-mark { width: 14px; height: 14px; }
  .card--front .brand-name { font-size: 28px; }
  .card--front .brand-tagline { font-size: 15px; margin-top: 8px; }

  .card--back .brand { left: 0; right: 0; top: 130px; }
  .card--back .brand-mark { width: 22px; height: 22px; }
  .card--back .brand-name { font-size: 46px; }
  .card--back .brand-tagline { font-size: 19px; margin-top: 12px; }
</style>
</head>
<body>

<section class="card card--front" aria-label="Business card front">
  <div class="profile">
    <div class="portrait" role="img" aria-label="Portrait photo of Owen Hale"></div>
    <h1 class="agent-name">Owen Hale</h1>
    <p class="agent-title">Managing Director</p>
    <ul class="contact-list">
      <li>
        <svg viewBox="0 0 16 16" aria-hidden="true"><path fill="var(--red)" d="M3.6 1.2l2.4 2.9-1.3 1.8c.9 2.1 2.3 3.6 4.4 4.6l1.8-1.3 2.9 2.4-1.4 2.6C7.2 13.9 2.1 8.8 1 3z"/></svg>
        123 456 789
      </li>
      <li>
        <svg viewBox="0 0 16 16" aria-hidden="true"><rect x="1" y="3" width="14" height="10" rx="1.5" fill="var(--red)"/><path d="M1.5 4l6.5 5 6.5-5" stroke="#fff" stroke-width="1.4" fill="none"/></svg>
        info@bloomferrykite.com
      </li>
      <li>
        <svg viewBox="0 0 16 16" aria-hidden="true"><circle cx="8" cy="8" r="7" fill="var(--red)"/><path d="M1 8h14M8 1c-3 3.5-3 10.5 0 14M8 1c3 3.5 3 10.5 0 14" stroke="#fff" stroke-width="1.1" fill="none"/></svg>
        www.bloomferrykite.com
      </li>
    </ul>
    <p class="address">48 Harbour Lane, Westport<br>Maine, 04101</p>
  </div>

  <div class="brand">
    <div class="brand-lockup">
      <span class="brand-mark" aria-hidden="true"></span>
      <p class="brand-name">Bloom Ferry Kite</p>
    </div>
    <p class="brand-tagline">Keeping Each Kite Aloft</p>
  </div>
</section>

<section class="card card--back" aria-label="Business card back">
  <div class="brand">
    <div class="brand-lockup">
      <span class="brand-mark" aria-hidden="true"></span>
      <p class="brand-name">Bloom Ferry Kite</p>
    </div>
    <p class="brand-tagline">Keeping Each Kite Aloft</p>
  </div>
</section>

</body>
</html>
```